Design and Renovation Company Luxury Business Card

I want to create a luxury business card for a Design and Renovation Firm . We will use our current logo. The company name is 742BUILD. We do not want anything standard. We need a very unique concept.
Please see uploaded inspiration. I really like the textured paper option. I would like the card to be thick with debossing, and/or embossing options. The logo has orange in it but I would like to see the card with and without the orange. I think the orange may make the company feel less high-end. The goal is to elevate the logo not match its vibe per se of the logo. We want something very unique, not standard at all!
I would like a space for :
Logo,
Name,
Position,
Email,
Office number,
Website Address,
Business Address,
Thank you!
Have fun!
Target Market(s)
Home owners Age 35 +
Industry/Entity Type
Design and Renovation
Contact Information for Business Card
Logo, Name, Position, Email, Office number, Website Address, Business Address,.
Colors
Designer to choose colors to be used in the design.
Requirements
Must have
- A luxury designer feel. Must be black or dark grey but open to other luxury ideas.
Nice to have
- Gold, silver, black embossing or debossing. Textured paper design.
Should not have
- A cheap look and feel.

```html
<!DOCTYPE html>
<html lang="en">
<head>
<meta charset="utf-8">
<title>742BUILD Business Card</title>
<link href="https://fonts.googleapis.com/css2?family=Roboto:wght@400;500;700&display=swap" rel="stylesheet">
<style>
  :root {
    --backdrop: #121212;
    --card: #161616;
    --tile-dark: #141414;
    --tile-light: #262626;
    --gold: #cfae62;
  }
  * { margin: 0; padding: 0; box-sizing: border-box; }
  html, body {
    width: 1200px; height: 900px; overflow: hidden;
    background: var(--backdrop);
    font-family: "Roboto", Arial, sans-serif;
    color: var(--gold);
  }
  .canvas {
    width: 1200px; height: 900px;
    display: flex; flex-direction: column; align-items: center; justify-content: center;
    gap: 36px;
  }
  .card {
    position: relative;
    width: 700px; height: 400px;
    background: var(--card);
    box-shadow: 0 10px 30px rgba(0,0,0,.7);
  }
  .tile-texture {
    position: absolute; inset: 0;
    background: linear-gradient(135deg, var(--tile-light) 0%, var(--tile-dark) 45%, var(--tile-light) 100%);
  }
  .brand-name {
    position: absolute; right: 48px; bottom: 52px;
    font-size: 40px; font-weight: 500; line-height: 1;
    color: var(--gold);
  }
  .person {
    position: absolute; left: 56px; top: 56px;
  }
  .person-name { font-size: 28px; font-weight: 700; line-height: 1.1; }
  .person-role { font-size: 20px; font-weight: 400; }
  .address {
    position: absolute; left: 56px; top: 200px;
    font-size: 19px; line-height: 1.3; font-style: normal;
  }
  .contacts {
    position: absolute; left: 56px; bottom: 40px;
    list-style: none; font-size: 19px; line-height: 1.45;
  }
  .contacts li { display: flex; align-items: center; gap: 10px; }
  .contacts svg { width: 18px; height: 18px; flex: none; }
</style>
</head>
<body>
<main class="canvas">
  <section class="card card-front">
    <div class="tile-texture" role="img" aria-label="Embossed dark square tile pattern across the card"></div>
    <span class="brand-name">742BUILD</span>
  </section>

  <section class="card card-back">
    <div class="person">
      <p class="person-name">MARCUS HALE</p>
      <p class="person-role">Managing Director</p>
    </div>
    <address class="address">
      18 Calder Row, Suite 4<br>60214, Westbrook
    </address>
    <ul class="contacts">
      <li>
        <svg viewBox="0 0 24 24" fill="none" stroke="currentColor" stroke-width="2"><path d="M5 3h4l2 5-2.5 1.5a11 11 0 0 0 6 6L16 13l5 2v4a2 2 0 0 1-2 2A16 16 0 0 1 3 5a2 2 0 0 1 2-2z"/></svg>
        044-987 654 321
      </li>
      <li>
        <svg viewBox="0 0 24 24" fill="none" stroke="currentColor" stroke-width="2"><rect x="3" y="5" width="18" height="14"/><path d="M3 5l9 8 9-8"/></svg>
        info@742build.com
      </li>
      <li>
        <svg viewBox="0 0 24 24" fill="none" stroke="currentColor" stroke-width="2"><circle cx="12" cy="12" r="9"/><path d="M3 12h18M12 3c3 3 3 15 0 18M12 3c-3 3-3 15 0 18"/></svg>
        www.742build.com
      </li>
    </ul>
    <span class="brand-name">742BUILD</span>
  </section>
</main>
</body>
</html>
```